Announcement for a New Trauma Therapy Group - Rack Card

I need a two-sided "rack" card that is 4x9 announcing a Women's Trauma and Loss Group. I am a licensed therapist and will be starting this support group for women who have experienced trauma of all kinds. In addition to groups, I offer individual, couples, and family counseling sessions.

I would like to see designs that are soft tones and use colors like muted blues, greens, and sand tones. The final design should communicate hope and healing as well as have a peaceful feel to it.

I would like a picture of a woman's profile from either the side or from behind her. (possibly a contemplative picture on a beach)

I am attaching a picture of myself to go alongside the bio information as well.

On One Side, I need the description of the group and contact info:

Healing the Hurting Heart
Women's Trauma & Loss Group
Led by Licensed Professional Counselor, Joy Belden Crane

10 Week Group
Cost - $35 session
Group size limited to 10 participants

Topics Include:
What is Trauma?
How Trauma Affects Us
Creating a Feeling of Safety
Managing Trauma Triggers
Importance of Self Care
Healthy vs. Unhealthy Coping
Guilt, Shame, and Blame
Victim vs. Victimized
Grieving through Loss
Anger and Forgiveness
Imagining a Better Future

For More Information, Contact:
Joy Belden Crane, LPC, LMFT
(555) 614-3928
joy@brightmeadowcare.example

On Side Two:

Life hurts and does not seem fair. So what do you do when you are faced with an event in your life that knocks you off your feet? It seems no one understands what you are feeling and no one knows just what to say. It is tempting to pull away and isolate or put up a mask and pretend everything is OK.

It is my desire you know that you are not alone! There are others who understand the feelings you are going through and offer a safe place for encouraging support. I want to invite you to embark on a courageous journey of healing where you will not only learn how to "survive" after trauma and loss, but instead, learn that you can once again "thrive"!
- Joy Belden Crane, LPC, LMFT

Joy Belden Crane is a Licensed Professional Counselor and Licensed Marriage and Family Therapist. She is the owner of Still Waters Counseling Services located in Tulsa, OK.

Joy is a trauma survivor herself and understands firsthand the unique challenges that can arise on the journey to healing.

(Include Joy's picture next to bio)

(Attach logo and business information to this side as well.)

Target Market(s)

Women who have gone through a traumatic experience or loss and are hurting emotionally

Industry/Entity Type

Counsellor

Font styles to use
Serif
Script

Colors
fbe7d2
86cfc6
cfeae6
85abd2
cfdeed

Requirements
Must have
• Joy's picture as well as her logo and contact information must be on the card.
• One side of the card should describe the group with the following description:
• "Healing the Hurting Heart"
• Women's Trauma & Loss Group
• Led by Licensed Professional Counselor, Joy Belden Crane
• 10 Week Group
• Cost - $35 session
• Group size limited to 10 participants
• Topics Include:
• What is Trauma?
• How Trauma Affects Us
• Creating a Feeling of Safety
• Managing Trauma Triggers
• Importance of Self Care
• Healthy vs. Unhealthy Coping
• Guilt, Shame, and Blame
• Victim vs. Victimized
• Grieving through Loss
• Anger and Forgiveness
• Imagining a Better Future
• For More Information, Contact:
• Joy Belden Crane, LPC, LMFT
• (555) 614-3928
• joy@brightmeadowcare.example
• On the second side, it must have this note from Joy:
• Life hurts and does not seem fair. So what do you do when you are faced with an event in your life that knocks you off your feet? It seems no one understands what you are feeling and no one knows just what to say. It is tempting to pull away and isolate or put up a mask and pretend everything is OK.
• It is my desire you know that you are not alone! There are others who understand the feelings you are going through and offer a safe place for encouraging support. I want to invite you to embark on a courageous journey of healing where you will not only learn how to "survive" after trauma and loss, but instead, learn that you can once again "thrive"!
• - Joy Belden Crane, LPC, LMFT
• Joy Belden Crane is a Licensed Professional Counselor and Licensed Marriage and Family Therapist. She is the owner of Still Waters Counseling Services located in Tulsa, OK.
• Joy is a trauma survivor herself and understands firsthand the unique challenges that can arise on the journey to healing. In addition to facilitating groups, Joy also offers individual, marriage, and family counseling.
Nice to have
• soft muted colors that are peaceful. Light blues, greens, sand colors would work well. A picture at the top of the card of either a woman or a woman's profile that is hopeful such as a woman sitting at a beach overlooking the ocean.
Should not have
• No harsh or bright bold colors. This card needs to have a peaceful feeling to it.

```html
<!DOCTYPE html>
<html lang="en">
<head>
<meta charset="utf-8">
<title>Healing the Hurting Heart – Rack Card</title>
<link rel="stylesheet" href="https://fonts.googleapis.com/css2?family=Lato:wght@400;700&family=Great+Vibes&family=Courgette&display=swap">
<style>
  :root{
    --page:#e9e9e9;
    --card:#ffffff;
    --blue:#3f78c0;
    --wave:#85abd2;
    --wave-light:#cfdeed;
    --teal:#86cfc6;
    --mist:#cfeae6;
    --sand:#fbe7d2;
    --green:#4f8a2b;
    --ink:#222222;
    --brown:#3b2216;
    --body:'Lato', Arial, sans-serif;
    --script:'Great Vibes', cursive;
    --hand:'Courgette', cursive;
  }
  *{box-sizing:border-box;margin:0;padding:0}
  html,body{width:800px;height:1200px;overflow:hidden;background:var(--page);font-family:var(--body);color:var(--ink)}
  .canvas{position:relative;width:800px;height:1200px}
  .card{position:absolute;top:195px;width:360px;height:810px;background:var(--card);overflow:hidden;box-shadow:0 6px 18px rgba(0,0,0,.25)}
  .card--front{left:30px}
  .card--back{left:410px}
  .layer{position:absolute;left:0;top:0}
  .brand{position:absolute;display:flex;align-items:center;gap:6px;font-family:var(--body);font-weight:700;color:var(--green);line-height:1.05}
  .brand__dot{width:22px;height:22px;border-radius:50%;background:var(--green);flex:none}
  .brand__name{font-size:14px}

  /* front */
  .hero-title{position:absolute;left:22px;top:140px;font-family:var(--script);color:#fff;font-size:36px;line-height:44px;text-shadow:0 1px 3px rgba(0,0,0,.4)}
  .group-title{position:absolute;left:22px;top:326px;font-size:20px;font-weight:700;color:var(--blue)}
  .group-lead{position:absolute;left:22px;top:354px;font-size:11px}
  .facts{position:absolute;left:22px;top:396px;list-style:none}
  .facts li{display:flex;align-items:center;gap:8px;font-size:14px;height:27px}
  .facts svg{width:14px;height:14px;flex:none}
  .topics-heading{position:absolute;left:38px;top:488px;font-family:var(--script);color:var(--blue);font-size:30px}
  .topics{position:absolute;top:548px;list-style:none}
  .topics--a{left:22px}
  .topics--b{left:194px}
  .topics li{display:flex;align-items:center;gap:6px;font-size:10.5px;height:15px}
  .topics svg{width:9px;height:9px;flex:none}
  .contact{position:absolute;left:22px;top:712px;font-size:11.5px;line-height:16px}
  .contact__label{font-weight:700}
  .contact__name{color:var(--green);margin-top:2px}
  .contact__row{display:flex;align-items:center;gap:6px;margin-top:3px}
  .contact__row svg{width:10px;height:10px}
  .portrait{position:absolute;right:0;bottom:0;width:125px;height:150px;background:linear-gradient(180deg,#e6cf9a,#6b3a4a);border-radius:62px 0 0 0}

  /* back */
  .quote-mark{position:absolute;font-family:Georgia,serif;font-weight:700;color:var(--brown);font-size:70px;line-height:1}
  .quote-mark--open{left:20px;top:70px}
  .quote-mark--close{right:20px;top:395px}
  .quote{position:absolute;left:22px;top:118px;width:312px;font-family:var(--hand);color:var(--blue);font-size:12.5px;line-height:16.6px}
  .quote p+p{margin-top:14px}
  .attribution{position:absolute;right:22px;top:445px;font-size:12.5px;color:var(--wave)}
  .bio-photo{position:absolute;left:22px;top:474px;width:120px;height:146px;background:linear-gradient(180deg,#bfd0e0,#d9c9a7);border:2px solid var(--wave);border-radius:3px}
  .bio{position:absolute;left:150px;top:478px;width:190px;font-size:10px;line-height:13.5px}
  .bio p+p{margin-top:10px}
  .card-info{position:absolute;left:145px;top:686px;font-size:9.4px;line-height:13px}
  .card-info__name{color:var(--blue);font-weight:700;font-size:11px}
  .card-info__title{padding-left:14px}
  .card-info__row{display:flex;gap:6px;align-items:flex-start}
  .card-info__row svg{width:9px;height:9px;margin-top:2px;flex:none}
  .divider{position:absolute;left:135px;top:690px;width:1px;height:108px;background:var(--wave-light)}
</style>
</head>
<body>
<main class="canvas">

  <!-- Front side -->
  <section class="card card--front" aria-label="Front side: group details">
    <svg class="layer" width="360" height="330" viewBox="0 0 360 330">
      <defs>
        <clipPath id="heroClip">
          <path d="M0 95 C110 60 240 40 360 45 L360 235 C260 265 140 275 0 240 Z"/>
        </clipPath>
        <linearGradient id="heroFill" x1="0" y1="0" x2="0" y2="1">
          <stop offset="0" stop-color="#9fb0bf"/>
          <stop offset=".45" stop-color="#6d7f8f"/>
          <stop offset=".75" stop-color="#3d4a52"/>
          <stop offset="1" stop-color="#5a5448"/>
        </linearGradient>
      </defs>
      <rect role="img" aria-label="Photo of a woman seen from behind, sitting on a beach looking out at the sea" clip-path="url(#heroClip)" x="0" y="0" width="360" height="300" fill="url(#heroFill)"/>
      <path d="M0 20 C40 70 120 75 200 60 C260 50 320 40 360 45 L360 52 C300 52 240 66 170 76 C90 86 30 70 0 40 Z" fill="var(--wave)"/>
      <path d="M0 88 C90 62 210 50 360 55 L360 60 C230 58 120 72 0 100 Z" fill="var(--teal)"/>
      <path d="M0 238 C120 275 260 270 360 232 L360 244 C250 285 110 285 0 252 Z" fill="var(--wave)"/>
      <path d="M0 256 C110 292 260 288 360 252 L360 256 C260 294 110 298 0 262 Z" fill="var(--wave-light)"/>
    </svg>
    <div class="brand" style="left:30px;top:22px"><span class="brand__dot"></span><span class="brand__name">Still Waters<br>Counseling</span></div>
    <h1 class="hero-title">Healing the<br>Hurting Heart</h1>

    <h2 class="group-title">Women's Trauma &amp; Loss Group</h2>
    <p class="group-lead">Led by Licensed Professional Counselor, Joy Belden Crane</p>

    <ul class="facts">
      <li><svg viewBox="0 0 14 14"><rect x="1" y="2.5" width="12" height="10.5" rx="1" fill="none" stroke="var(--wave)" stroke-width="1.4"/><path d="M1 6h12M4 1v3M10 1v3" stroke="var(--wave)" stroke-width="1.4"/></svg>10 Week Group</li>
      <li><svg viewBox="0 0 14 14"><path d="M10 3.5C9 2.3 4 2 4 4.8S10 7 10 9.6 5 12 3.8 10.5M7 1v12" fill="none" stroke="var(--wave)" stroke-width="1.4"/></svg>Cost - $35 session</li>
      <li><svg viewBox="0 0 14 14"><circle cx="5" cy="4" r="2.2" fill="none" stroke="var(--wave)" stroke-width="1.3"/><circle cx="10" cy="5" r="1.8" fill="none" stroke="var(--wave)" stroke-width="1.3"/><path d="M1 13c0-3 2-4.5 4-4.5S9 10 9 13M9.5 8.5c2 0 3.5 1.3 3.5 4" fill="none" stroke="var(--wave)" stroke-width="1.3"/></svg>Group size limited to 10 participants</li>
    </ul>

    <h3 class="topics-heading">Topics:</h3>
    <ul class="topics topics--a">
      <li><svg viewBox="0 0 10 10"><circle cx="5" cy="5" r="4.2" fill="none" stroke="#555" stroke-width="1"/><path d="M3 5l1.5 1.5L7.5 3" fill="none" stroke="#555" stroke-width="1.2"/></svg>What is Trauma?</li>
      <li><svg viewBox="0 0 10 10"><circle cx="5" cy="5" r="4.2" fill="none" stroke="#555" stroke-width="1"/><path d="M3 5l1.5 1.5L7.5 3" fill="none" stroke="#555" stroke-width="1.2"/></svg>How Trauma Affects Us</li>
      <li><svg viewBox="0 0 10 10"><circle cx="5" cy="5" r="4.2" fill="none" stroke="#555" stroke-width="1"/><path d="M3 5l1.5 1.5L7.5 3" fill="none" stroke="#555" stroke-width="1.2"/></svg>Creating a Feeling of Safety</li>
      <li><svg viewBox="0 0 10 10"><circle cx="5" cy="5" r="4.2" fill="none" stroke="#555" stroke-width="1"/><path d="M3 5l1.5 1.5L7.5 3" fill="none" stroke="#555" stroke-width="1.2"/></svg>Managing Trauma Triggers</li>
      <li><svg viewBox="0 0 10 10"><circle cx="5" cy="5" r="4.2" fill="none" stroke="#555" stroke-width="1"/><path d="M3 5l1.5 1.5L7.5 3" fill="none" stroke="#555" stroke-width="1.2"/></svg>Importance of Self Care</li>
      <li><svg viewBox="0 0 10 10"><circle cx="5" cy="5" r="4.2" fill="none" stroke="#555" stroke-width="1"/><path d="M3 5l1.5 1.5L7.5 3" fill="none" stroke="#555" stroke-width="1.2"/></svg>Healthy vs. Unhealthy Coping</li>
    </ul>
    <ul class="topics topics--b">
      <li><svg viewBox="0 0 10 10"><circle cx="5" cy="5" r="4.2" fill="none" stroke="#555" stroke-width="1"/><path d="M3 5l1.5 1.5L7.5 3" fill="none" stroke="#555" stroke-width="1.2"/></svg>Guilt, Shame, and Blame</li>
      <li><svg viewBox="0 0 10 10"><circle cx="5" cy="5" r="4.2" fill="none" stroke="#555" stroke-width="1"/><path d="M3 5l1.5 1.5L7.5 3" fill="none" stroke="#555" stroke-width="1.2"/></svg>Victim vs. Victimized</li>
      <li><svg viewBox="0 0 10 10"><circle cx="5" cy="5" r="4.2" fill="none" stroke="#555" stroke-width="1"/><path d="M3 5l1.5 1.5L7.5 3" fill="none" stroke="#555" stroke-width="1.2"/></svg>Grieving through Loss</li>
      <li><svg viewBox="0 0 10 10"><circle cx="5" cy="5" r="4.2" fill="none" stroke="#555" stroke-width="1"/><path d="M3 5l1.5 1.5L7.5 3" fill="none" stroke="#555" stroke-width="1.2"/></svg>Anger and Forgiveness</li>
      <li><svg viewBox="0 0 10 10"><circle cx="5" cy="5" r="4.2" fill="none" stroke="#555" stroke-width="1"/><path d="M3 5l1.5 1.5L7.5 3" fill="none" stroke="#555" stroke-width="1.2"/></svg>Imagining a Better Future</li>
    </ul>

    <svg class="layer" style="top:640px" width="360" height="60" viewBox="0 0 360 60">
      <path d="M0 45 C90 10 220 5 360 30 L360 38 C220 15 100 20 0 55 Z" fill="var(--wave)"/>
      <path d="M0 56 C100 24 230 20 360 42 L360 45 C230 26 100 30 0 60 Z" fill="var(--wave-light)"/>
    </svg>
    <div class="portrait" role="img" aria-label="Portrait photo of the counselor"></div>

    <div class="contact">
      <p class="contact__label">For More Information<br>Contact:</p>
      <p class="contact__name">Joy Belden Crane, LPC, LMFT</p>
      <p class="contact__row"><svg viewBox="0 0 10 10"><circle cx="5" cy="5" r="5" fill="var(--green)"/><path d="M3.3 2.6l1 1.2-.6.7c.4.8 1 1.4 1.8 1.8l.7-.6 1.2 1-.6.9C4.6 7.4 2.6 5.4 2.4 3.2z" fill="#fff"/></svg>(555) 614-3928</p>
      <p class="contact__row"><svg viewBox="0 0 10 10"><rect x="0.5" y="2" width="9" height="6.5" fill="var(--green)"/><path d="M.5 2l4.5 3.5L9.5 2" fill="none" stroke="#fff" stroke-width=".9"/></svg>joy@brightmeadowcare.example</p>
    </div>
  </section>

  <!-- Back side -->
  <section class="card card--back" aria-label="Back side: note and bio">
    <svg class="layer" width="360" height="60" viewBox="0 0 360 60">
      <path d="M0 0 H360 V30 C240 12 120 20 0 34 Z" fill="var(--wave)"/>
      <path d="M0 40 C120 24 240 18 360 34 L360 38 C240 24 120 30 0 44 Z" fill="var(--wave)"/>
    </svg>
    <span class="quote-mark quote-mark--open">&ldquo;</span>
    <div class="quote">
      <p>Life hurts and does not seem fair. So what do you do when you are faced with an event in your life that knocks you off your feet? It seems no one understands what you are feeling and no one knows just what to say. It is tempting to pull away and isolate or put up a mask and pretend everything is OK.</p>
      <p>It is my desire you know that you are not alone! There are others who understand the feelings you are going through and offer a safe place for encouraging support. I want to invite you to embark on a courageous journey of healing where you will not only learn how to "survive" after trauma and loss, but instead, learn that you can once again "thrive"!</p>
    </div>
    <span class="quote-mark quote-mark--close">&rdquo;</span>
    <p class="attribution">- Joy Belden Crane, LPC, LMFT</p>

    <div class="bio-photo" role="img" aria-label="Photo of the counselor sitting on a beach"></div>
    <div class="bio">
      <p>Joy Belden Crane is a Licensed Professional Counselor and Licensed Marriage and Family Therapist. She is the owner of Still Waters Counseling Services located in Tulsa, OK.</p>
      <p>Joy is a trauma survivor herself and understands firsthand the unique challenges that can arise on the journey to healing.</p>
    </div>

    <svg class="layer" style="top:622px" width="360" height="60" viewBox="0 0 360 60">
      <path d="M0 50 C120 20 240 10 360 20 L360 28 C240 20 120 30 0 58 Z" fill="var(--wave)"/>
      <path d="M0 30 C100 10 240 0 360 8 L360 11 C240 4 100 14 0 34 Z" fill="var(--wave-light)"/>
    </svg>
    <div class="brand" style="left:18px;top:725px"><span class="brand__dot"></span><span class="brand__name">Still Waters<br>Counseling</span></div>
    <div class="divider"></div>
    <div class="card-info">
      <p class="card-info__name">Joy Crane, LPC, LMFT</p>
      <p class="card-info__title">Licensed Professional Counselor<br>Licensed Marriage and Family Therapist</p>
      <p class="card-info__row"><svg viewBox="0 0 10 10"><path d="M5 10C2 6 1.5 4.8 1.5 3.5a3.5 3.5 0 017 0C8.5 4.8 8 6 5 10z" fill="var(--blue)"/><circle cx="5" cy="3.5" r="1.3" fill="#fff"/></svg><span>1240 Willow Bend Rd, Suite 300 Tulsa,<br>OK 74105</span></p>
      <p class="card-info__row"><svg viewBox="0 0 10 10"><circle cx="5" cy="5" r="5" fill="var(--blue)"/><path d="M3.3 2.6l1 1.2-.6.7c.4.8 1 1.4 1.8 1.8l.7-.6 1.2 1-.6.9C4.6 7.4 2.6 5.4 2.4 3.2z" fill="#fff"/></svg>(555) 614-3928</p>
      <p class="card-info__row"><svg viewBox="0 0 10 10"><rect x="0.5" y="2" width="9" height="6.5" fill="var(--blue)"/><path d="M.5 2l4.5 3.5L9.5 2" fill="none" stroke="#fff" stroke-width=".9"/></svg>joy@brightmeadowcare.example</p>
      <p class="card-info__row"><svg viewBox="0 0 10 10"><circle cx="5" cy="5" r="4.3" fill="none" stroke="var(--blue)" stroke-width="1.1"/><path d="M.7 5h8.6M5 .7c2 2.4 2 6.2 0 8.6M5 .7c-2 2.4-2 6.2 0 8.6" fill="none" stroke="var(--blue)" stroke-width=".8"/></svg>www.brightmeadowcare.example</p>
    </div>
  </section>

</main>
</body>
</html>
```